Financial Advisor Resource Firm needs business card design

Need business card design for company in Omaha NE called Tallowbrook Partners. We provide resources to financial advisors....workshop programs, retirement analysis, and insurance planning. I would like to see designs that use grays, greens, black, and white colors. The final design should communicate 'collaboration' and be simple yet attractive to financial planning clients. I will attached our logo and another picture of a puzzle piece coming together. I would like the incorporate the puzzle picture somehow, maybe on the back somehow, with color or just the gray scale....OR, the picture be the front of the card with 'Tallowbrook' definition on it (see upload) and then company logo, employee name, title, address on the back (see ppt uploaded). The following disclosure needs to be included somewhere- Advisory services offered through Marlowe Ridge Advisors, LLC.
Updates

I uploaded a svg and ai file of the logo

Target Market(s)

Financial planning clients and financial advisors....so pretty diverse age range of about 40-70.

Industry/Entity Type

Financial Planning

Contact Information for Business Card

Dennis K. Holloway, MBA
Founder/President
5727 E. Larkspur Avenue
Suite 418
Omaha, NE 68297
Phone- (402) 555-0147
Cell- (402) 555-0183
Fax- (402) 555-0129
email- dennis@tallowbrookgroup.example
web address- www.tallowbrookgroup.example

Colors
1b1b1b
474747
d3d3d3
ffffff
9bcb3c
abd036

Requirements
Must have
• Must include logo provided, must be 2 sided, and must have disclosure...all of these items listed in project description

```html
<!DOCTYPE html>
<html lang="en">
<head>
<meta charset="utf-8">
<title>Tallowbrook Partners – Business Card</title>
<link rel="stylesheet" href="https://fonts.googleapis.com/css2?family=Tinos:wght@400;700&display=swap">
<style>
  :root {
    --ink: #1b1b1b;
    --charcoal: #474747;
    --mist: #d3d3d3;
    --paper: #ffffff;
    --leaf: #9bcb3c;
    --lime: #abd036;
    --backdrop: #e4e4e4;
    --fine-print: #a8a8a8;
  }
  * { box-sizing: border-box; margin: 0; padding: 0; }
  html, body {
    width: 1200px; height: 864px; overflow: hidden;
    background: var(--backdrop);
    font-family: "Tinos", "Times New Roman", serif;
    color: var(--ink);
  }
  .canvas { position: relative; width: 1200px; height: 864px; }

  .card {
    position: absolute; width: 620px; height: 354px;
    overflow: hidden;
    box-shadow: 0 6px 18px rgba(0,0,0,0.18);
  }

  /* Back side */
  .card--back { left: 520px; top: 60px; background: var(--charcoal); }
  .card__photo {
    position: absolute; inset: 0;
    background:
      radial-gradient(ellipse at 55% 70%, rgba(140,140,140,0.55), transparent 60%),
      linear-gradient(135deg, #3a3a3a 0%, #5a5a5a 45%, #2a2a2a 100%);
  }
  .definition {
    position: absolute; left: 0; right: 0; top: 70px;
    text-align: center; color: var(--paper);
  }
  .definition__word {
    font-size: 40px; font-weight: 400; color: var(--lime);
    letter-spacing: 1px; margin-left: 60px;
  }
  .definition__phonetic { font-size: 13px; margin-top: 6px; margin-left: 90px; }
  .definition__meaning { font-size: 15px; margin-top: 10px; margin-left: 40px; }
  .definition__web { font-size: 21px; letter-spacing: 0.5px; margin-top: 30px; }

  /* Front side */
  .card--front { left: 60px; top: 440px; background: var(--paper); }
  .brand {
    position: absolute; left: 40px; top: 42px;
    display: flex; align-items: center; gap: 12px;
  }
  .brand__dot { width: 22px; height: 22px; border-radius: 50%; background: var(--leaf); }
  .brand__name { font-size: 38px; font-weight: 700; color: var(--ink); letter-spacing: 0.5px; }
  .disclosure {
    position: absolute; left: 40px; top: 98px;
    font-size: 10px; color: var(--fine-print); letter-spacing: 0.2px;
  }
  .rule {
    position: absolute; left: 40px; top: 122px; width: 310px; height: 2px;
    background: var(--ink);
  }
  .contacts {
    position: absolute; left: 40px; top: 140px;
    list-style: none; font-size: 15px; line-height: 21px;
  }
  .contacts li { display: flex; align-items: center; gap: 10px; }
  .contacts svg { width: 12px; height: 12px; fill: var(--leaf); flex: none; }
  .person { position: absolute; left: 345px; top: 150px; }
  .person__name { font-size: 21px; font-weight: 700; }
  .person__title { font-size: 15px; font-weight: 700; color: var(--leaf); }
  .address {
    position: absolute; left: 345px; top: 238px;
    font-style: normal; font-size: 15px; line-height: 19px;
  }
</style>
</head>
<body>
<main class="canvas">

  <section class="card card--back" aria-label="Card back">
    <div class="card__photo" role="img" aria-label="Grayscale photo of hands bringing puzzle pieces together"></div>
    <div class="definition">
      <p class="definition__word">TAL·LOW·BROOK</p>
      <p class="definition__phonetic">ˈta·lō·brŏŏk</p>
      <p class="definition__meaning">: to come together and unite in common interest and focus</p>
      <p class="definition__web">www.tallowbrookgroup.example</p>
    </div>
  </section>

  <section class="card card--front" aria-label="Card front">
    <div class="brand">
      <span class="brand__dot"></span>
      <span class="brand__name">Tallowbrook Partners</span>
    </div>
    <p class="disclosure">Advisory services offered through Marlowe Ridge Advisors, LLC</p>
    <div class="rule"></div>

    <ul class="contacts">
      <li>
        <svg viewBox="0 0 12 12" aria-label="Cell"><path d="M3 0h6a1 1 0 0 1 1 1v10a1 1 0 0 1-1 1H3a1 1 0 0 1-1-1V1a1 1 0 0 1 1-1zm0 2v7h6V2z"/></svg>
        (402) 555-0183
      </li>
      <li>
        <svg viewBox="0 0 12 12" aria-label="Fax"><path d="M3 0h6v4H3zM1 5h10v5H9v2H3v-2H1zm3 4v2h4V9z"/></svg>
        (402) 555-0129
      </li>
      <li>
        <svg viewBox="0 0 12 12" aria-label="Phone"><path d="M2 1h3l1 3-1.5 1a7 7 0 0 0 2.5 2.5L8 6l3 1v3a1 1 0 0 1-1 1A9 9 0 0 1 1 2a1 1 0 0 1 1-1z"/></svg>
        (402) 555-0147
      </li>
      <li>
        <svg viewBox="0 0 12 12" aria-label="Email"><path d="M0 2h12v8H0zm1 1v.4l5 3.2 5-3.2V3z"/></svg>
        dennis@tallowbrookgroup.example
      </li>
    </ul>

    <div class="person">
      <p class="person__name">Dennis K. Holloway, MBA</p>
      <p class="person__title">Founder/President</p>
    </div>

    <address class="address">
      5727 E. Larkspur Avenue<br>
      Suite 418<br>
      Omaha, NE 68297
    </address>
  </section>

</main>
</body>
</html>
```